Airport sign

Design a 1 mt x 2 mt (landscape) sign for display at our domestic/international terminal called Mavuni airport - 65% devoted to the resort and 35% to Lorvan Reef Dive
Full colour - one sign is located in the arrivals area as people wait for customs checks - the other will be located in the domestic arrivals and departure area on the orange wall in photo

```html
<!DOCTYPE html>
<html lang="en">
<head>
<meta charset="utf-8">
<title>Shorecrest Resort – Airport Sign</title>
<link rel="stylesheet" href="https://fonts.googleapis.com/css2?family=Montserrat:wght@700;800;900&display=swap">
<style>
  :root{
    --backdrop:#141416;
    --panel-light:#f7f8f9;
    --panel-shade:#e3e6e9;
    --navy:#134a66;
    --navy-deep:#0f2f52;
    --green:#5b8c35;
    --green-bright:#6fa23e;
    --sky:#1aa8e0;
    --white:#ffffff;
  }
  *{margin:0;padding:0;box-sizing:border-box}
  html,body{width:1200px;height:766px;overflow:hidden;background:var(--backdrop)}
  body{font-family:"Montserrat",Verdana,sans-serif;position:relative}
  .sign{position:absolute;left:70px;top:118px;width:1058px;height:528px;overflow:hidden;
    background:radial-gradient(ellipse at 50% 40%,var(--panel-light) 0%,var(--panel-shade) 100%)}
  .swoosh{position:absolute;left:0;top:0;width:1058px;height:528px}
  .resort-title{position:absolute;left:36px;top:30px;color:var(--navy);font-weight:900;line-height:.95}
  .resort-title .line-1{display:block;font-size:62px;letter-spacing:1px}
  .resort-title .line-2{display:block;font-size:94px;letter-spacing:1px}
  .resort-contact{position:absolute;left:28px;top:198px;width:468px;height:83px;border-radius:20px;
    background:linear-gradient(90deg,var(--green),var(--green-bright));color:var(--white);
    text-align:center;font-weight:700;font-size:16.5px;line-height:19.5px;padding-top:13px}
  .checklist{position:absolute;list-style:none;color:var(--navy-deep);font-weight:700;font-size:16.5px}
  .checklist li{display:flex;align-items:center;gap:6px;height:19.4px}
  .checklist svg{width:16px;height:16px;flex:none}
  .resort-features{left:30px;top:301px}
  .dive-features{left:654px;top:270px;font-size:17px}
  .dive-features li{gap:14px}
  .dive-title{position:absolute;left:655px;top:30px;color:var(--navy-deep);font-weight:900;font-size:49px;line-height:54px;letter-spacing:.5px}
  .dive-contact{position:absolute;left:608px;top:145px;width:463px;height:110px;background:var(--sky);
    border-radius:0 30px 30px 0;color:var(--white);font-weight:700;font-size:17px;line-height:21px;padding:12px 0 0 46px}
  .brand{position:absolute;display:flex;align-items:center;gap:10px;font-weight:800;font-size:24px}
  .brand-resort{left:318px;top:438px;color:var(--navy)}
  .brand-resort .dot{width:46px;height:46px;border-radius:50%;background:var(--green-bright)}
  .brand-dive{left:656px;top:400px;color:var(--navy-deep);font-size:22px;line-height:26px}
  .brand-dive .dot{width:96px;height:96px;border-radius:50%;background:var(--sky)}
</style>
</head>
<body>
<svg width="0" height="0" style="position:absolute">
  <symbol id="tick" viewBox="0 0 16 16">
    <circle cx="7.5" cy="8.5" r="6" fill="none" stroke="currentColor" stroke-width="1.8"/>
    <path d="M4.5 8.5 L7.3 11 L15 2.5" fill="none" stroke="currentColor" stroke-width="2" stroke-linecap="round"/>
  </symbol>
</svg>

<main class="sign">
  <svg class="swoosh" viewBox="0 0 1058 528" aria-hidden="true">
    <path d="M540 0 C600 70 640 160 640 260 C640 380 660 470 740 528 L700 528 C620 470 610 380 610 260 C610 150 580 70 520 0 Z" fill="var(--navy-deep)"/>
    <path d="M488 0 C570 80 592 170 592 270 C592 390 620 470 705 528 L668 528 C585 470 575 390 575 270 C575 170 550 80 470 0 Z" fill="var(--green-bright)"/>
    <path d="M510 0 C588 80 606 170 606 270 C606 390 634 470 720 528 L705 528 C620 470 592 390 592 270 C592 170 572 80 488 0 Z" fill="var(--navy)"/>
  </svg>

  <h1 class="resort-title"><span class="line-1">SHORECREST</span><span class="line-2">RESORT</span></h1>

  <div class="resort-contact">
    <p>Palm Corner, Kavora | Ph+ (600) 41 502</p>
    <p>Stay@TheShorecrestResort.com</p>
    <p>TheShorecrestResort.com</p>
  </div>

  <ul class="checklist resort-features">
    <li><svg><use href="#tick"/></svg>Air Con Accommodation</li>
    <li><svg><use href="#tick"/></svg>Free Wifi</li>
    <li><svg><use href="#tick"/></svg>Bungalows</li>
    <li><svg><use href="#tick"/></svg>Family Apartments</li>
    <li><svg><use href="#tick"/></svg>Restaurant &amp; Bar</li>
    <li><svg><use href="#tick"/></svg>Swimming Pool</li>
    <li><svg><use href="#tick"/></svg>Beach Frontage</li>
    <li><svg><use href="#tick"/></svg>Close to Town &amp; Airport</li>
    <li><svg><use href="#tick"/></svg>Sea Breezes</li>
    <li><svg><use href="#tick"/></svg>Scuba Diving</li>
  </ul>

  <div class="brand brand-resort"><span>Shorecrest Resort</span><span class="dot"></span></div>

  <h2 class="dive-title">LORVAN REEF<br>DIVE &amp; FISH</h2>

  <div class="dive-contact">
    <p>Located at Shorecrest Resort</p>
    <p>Ph: + (600) 72 46 193</p>
    <p>reefdesk@lorvanmail.com</p>
    <p>LorvanReefDive.com</p>
  </div>

  <ul class="checklist dive-features">
    <li><svg><use href="#tick"/></svg>Boat Dives</li>
    <li><svg><use href="#tick"/></svg>International Diver Training</li>
    <li><svg><use href="#tick"/></svg>Snorkeling Safaris</li>
    <li><svg><use href="#tick"/></svg>Fishing Charters</li>
  </ul>

  <div class="brand brand-dive"><span class="dot"></span><span>Lorvan Reef<br>Dive &amp; Fish</span></div>
</main>
</body>
</html>
```